Referring Dentists Referral Card

Corwell Pediatric & Teen Dentistry is looking for a new referral card to give to dentists sending their patients to our office for special treatment. Corwell Pediatric & Teen Dentistry is a modern, fun, and safe environment for children and teens to receive and experience the highest quality of dental care available. At CPTD we believe in shaping a positive experience for your child so they look forward to and love coming to the dentist!

Target Market(s)

Dentists

Industry/Entity Type

Dental

Font styles to use
Sans Serif

Colors
0292cd
acd036
f37122

Requirements
Must have
• Logo, phone number, copy from file "Referral Card In"

```html
<!DOCTYPE html>
<html lang="en">
<head>
<meta charset="utf-8">
<title>Corwell Pediatric &amp; Teen Dentistry — Referral Card</title>
<link href="https://fonts.googleapis.com/css2?family=Questrial&family=Dancing+Script:wght@500&family=Montserrat:wght@600&display=swap" rel="stylesheet">
<style>
  :root{
    --green:#5fa619;
    --orange:#f15a22;
    --teal:#1a8ba3;
    --teal-text:#2196a9;
    --white:#ffffff;
    --backdrop:#e9e6e1;
    --art-skin:#d9b98a;
  }
  *{box-sizing:border-box;margin:0;padding:0}
  html,body{width:1200px;height:900px;overflow:hidden;background:var(--backdrop)}
  body{position:relative;font-family:'Questrial',sans-serif}
  .card{position:absolute;top:80px;width:340px;height:740px;background:var(--white);overflow:hidden;box-shadow:0 4px 14px rgba(0,0,0,.18)}
  .card--form{left:247px}
  .card--promo{left:618px}

  .brand{display:flex;align-items:center;gap:10px;font-family:'Questrial',sans-serif;line-height:1.05}
  .brand__dot{width:34px;height:34px;border-radius:50%;flex:none}
  .brand__name{font-size:19px}

  .form-head{position:absolute;left:0;top:0;width:100%;height:110px;background:var(--green);display:flex;align-items:center;justify-content:center}
  .form-head .brand__dot{background:var(--white)}
  .form-head .brand__name{color:var(--white)}
  .notice{position:absolute;left:0;top:115px;width:100%;height:55px;background:var(--orange);color:var(--white);font-family:'Dancing Script',cursive;font-size:21px;display:flex;align-items:center;justify-content:center;white-space:nowrap}
  .intro{position:absolute;left:42px;right:42px;top:192px;text-align:center;color:var(--teal-text);font-size:16px;line-height:1.18;letter-spacing:.3px}
  .intro p+p{margin-top:18px}
  .doctors{position:absolute;left:0;right:0;top:383px;text-align:center;color:var(--teal-text);font-size:16px;line-height:1.2}
  .field{position:absolute;left:24px;right:21px}
  .field__label{color:var(--green);font-family:'Montserrat',sans-serif;font-weight:600;font-size:12.5px}
  .field__box{height:15px;border:1px solid var(--orange);margin-top:1px}
  .field--patient{top:437px}
  .field--doctor{top:470px}
  .checks{position:absolute;left:48px;top:508px;list-style:none;color:var(--orange);font-size:14px;line-height:17.5px}
  .checks li{display:flex;align-items:center;gap:8px}
  .checks li::before{content:"";width:9px;height:9px;border:1px solid var(--orange)}
  .comments{position:absolute;left:20px;top:568px;color:var(--green);font-family:'Montserrat',sans-serif;font-weight:600;font-size:12.5px}
  .rule{position:absolute;height:1px;background:var(--orange);opacity:.7}
  .form-foot{position:absolute;left:0;bottom:0;width:100%;height:55px;background:var(--teal)}
  .site{position:absolute;color:var(--white);font-size:17px;white-space:nowrap}
  .form-foot .site{left:55px;top:18px;font-size:15px}
  .form-art{position:absolute;right:17px;bottom:0;width:90px;height:120px;background:linear-gradient(180deg,var(--art-skin),#2a2a2a 60%);border-radius:18px 18px 0 0}

  .promo-head{position:absolute;left:48px;top:45px}
  .promo-head .brand__dot{width:42px;height:42px;background:var(--orange)}
  .promo-head .brand__name{color:var(--orange);font-size:24px}
  .team-band{position:absolute;left:0;top:328px;width:100%;height:113px;background:var(--teal)}
  .team-art{position:absolute;left:50px;top:115px;width:250px;height:326px;background:linear-gradient(180deg,#c99a3a 0%,var(--art-skin) 30%,#222 60%,#1b1b1b 100%);border-radius:40px 40px 0 0;opacity:.92}
  .tag{position:absolute;background:var(--orange);color:var(--white);font-size:11px;padding:2px 6px;white-space:nowrap}
  .tag--one{left:28px;top:364px}
  .tag--two{left:193px;top:355px;font-size:13px}
  .map{position:absolute;left:0;top:442px;width:100%;height:180px;background:linear-gradient(135deg,#f3f6f7,#dbeef2)}
  .contact{position:absolute;left:0;top:624px;width:100%;height:46px;background:var(--orange);color:var(--white);font-size:8.5px;line-height:1.35;display:flex;padding:10px 14px 0 22px;gap:10px}
  .contact__item{display:flex;gap:5px;align-items:flex-start}
  .contact__item svg{flex:none;margin-top:1px}
  .promo-foot{position:absolute;left:0;bottom:0;width:100%;height:68px;display:flex}
  .promo-foot__site{width:208px;background:var(--green);position:relative;border-right:3px solid var(--white)}
  .promo-foot__site .site{left:16px;top:24px;font-size:15.5px}
  .promo-foot__cert{flex:1;background:var(--teal);display:flex;align-items:center;padding-left:10px}
  .cert-badge{width:22px;height:22px;background:var(--white);opacity:.9}
</style>
</head>
<body>

<section class="card card--form">
  <header class="form-head">
    <div class="brand"><span class="brand__dot"></span><span class="brand__name">Corwell Pediatric<br>&amp; Teen Dentistry</span></div>
  </header>
  <div class="notice">Please bring this form to your appointment</div>
  <div class="intro">
    <p>Your dentist cares for the wellbeing of your child by referring to the pediatric dental specialists at Corwell Pediatric &amp; Teen Dentistry.</p>
    <p>our office does not provide oral conscious sedation</p>
  </div>
  <div class="doctors">Aaron Lindqvist, DDS MSD<br>Mason Pellham, DDS</div>
  <div class="field field--patient"><div class="field__label">Patient name</div><div class="field__box"></div></div>
  <div class="field field--doctor"><div class="field__label">Refering doctor</div><div class="field__box"></div></div>
  <ul class="checks">
    <li>Consultation for general anasthesia</li>
    <li>Complex dental needs</li>
    <li>Dental anxiety</li>
  </ul>
  <div class="comments">Comments:</div>
  <div class="rule" style="left:95px;right:21px;top:576px"></div>
  <div class="rule" style="left:20px;right:21px;top:593px"></div>
  <div class="rule" style="left:20px;right:21px;top:609px"></div>
  <div class="rule" style="left:20px;right:112px;top:625px"></div>
  <div class="rule" style="left:20px;right:112px;top:641px"></div>
  <div class="rule" style="left:20px;right:112px;top:657px"></div>
  <div class="rule" style="left:20px;right:112px;top:673px"></div>
  <footer class="form-foot"><span class="site">corwellkidsdentist.com</span></footer>
  <div class="form-art" role="img" aria-label="Illustration of the two dentists standing with crossed arms"></div>
</section>

<section class="card card--promo">
  <div class="promo-head brand"><span class="brand__dot"></span><span class="brand__name">Corwell Pediatric<br>&amp; Teen Dentistry</span></div>
  <div class="team-band"></div>
  <div class="team-art" role="img" aria-label="Illustration of the two dentists in black scrubs with crossed arms"></div>
  <span class="tag tag--one">Aaron Lindqvist, DDS MSD</span>
  <span class="tag tag--two">Mason Pellham, DDS</span>
  <div class="map" role="img" aria-label="Map showing the office location near the lake and highways"></div>
  <div class="contact">
    <div class="contact__item">
      <svg width="8" height="10" viewBox="0 0 8 10"><path d="M4 0a4 4 0 0 1 4 4c0 3-4 6-4 6S0 7 0 4a4 4 0 0 1 4-4z" fill="#fff"/><circle cx="4" cy="4" r="1.4" fill="#f15a22"/></svg>
      <span>240 N. Harbor Avenue Suite 118<br>Corwell, OK 73099</span>
    </div>
    <div class="contact__item">
      <svg width="9" height="22" viewBox="0 0 9 22"><path d="M2 0l2 2.5-1.3 1.5a6 6 0 0 0 2.4 2.4L6.5 5 9 7l-1.5 1.8C4 8.5.5 5 .2 1.5z" fill="#fff"/><rect x=".5" y="14" width="8" height="6" fill="none" stroke="#fff" stroke-width=".9"/><path d="M.5 14l4 3.5 4-3.5" fill="none" stroke="#fff" stroke-width=".9"/></svg>
      <span>405.555.0142<br>admin@corwellkidsdentist.com</span>
    </div>
  </div>
  <footer class="promo-foot">
    <div class="promo-foot__site"><span class="site">corwellkidsdentist.com</span></div>
    <div class="promo-foot__cert"><span class="cert-badge"></span></div>
  </footer>
</section>

</body>
</html>
```